Medical Company in need of Modern business card design for new Wound Care clinic.

Modern business card design for our Woundcare company. Logo and description of services can be found on our website; https://www.tornvel-skinheal.com/

```html
<!DOCTYPE html>
<html lang="en">
<head>
<meta charset="UTF-8">
<title>Tornvel Skinheal – Business Card</title>
<link rel="stylesheet" href="https://fonts.googleapis.com/css2?family=Montserrat:wght@400;500;600&family=Oswald:wght@500;600&display=swap">
<style>
  :root {
    --stage: #3a3a3a;
    --card-white: #ffffff;
    --card-black: #161616;
    --gold: #c9922e;
    --ink: #1f1f1f;
    --band-text: #f2f2f2;
  }
  * { box-sizing: border-box; margin: 0; padding: 0; }
  html, body { width: 1200px; height: 1200px; overflow: hidden; }
  body {
    background: var(--stage);
    font-family: "Montserrat", sans-serif;
    position: relative;
  }
  .card {
    position: absolute;
    left: 170px;
    width: 860px;
    height: 492px;
    border-radius: 34px;
    overflow: hidden;
  }
  .card--front { top: 70px; background: var(--card-white); }
  .card--back { top: 638px; background: var(--card-black); }

  /* Front */
  .brand-mark {
    position: absolute;
    top: 56px;
    right: 60px;
    display: flex;
    align-items: center;
    gap: 14px;
  }
  .brand-mark__square { width: 26px; height: 26px; background: var(--gold); }
  .brand-mark__name {
    font-weight: 600;
    font-size: 30px;
    letter-spacing: 3px;
    color: var(--gold);
  }
  .identity { position: absolute; left: 58px; top: 120px; }
  .identity__name {
    font-weight: 500;
    font-size: 40px;
    letter-spacing: 1px;
    color: var(--gold);
    line-height: 1;
  }
  .identity__title {
    font-size: 20px;
    color: var(--ink);
    margin-top: 6px;
    letter-spacing: 0.5px;
  }
  .contacts { list-style: none; margin-top: 14px; }
  .contacts li {
    display: flex;
    align-items: flex-start;
    gap: 14px;
    font-size: 21px;
    color: var(--ink);
    line-height: 1.2;
    margin-bottom: 6px;
  }
  .contacts svg { width: 22px; height: 22px; flex: none; margin-top: 1px; }

  .services-heading {
    position: absolute;
    left: 480px;
    top: 322px;
    font-family: "Oswald", sans-serif;
    font-weight: 600;
    font-size: 22px;
    color: var(--gold);
    letter-spacing: 0.5px;
  }
  .services-band {
    position: absolute;
    left: 0; right: 0;
    top: 364px;
    height: 104px;
    background: var(--card-black);
    display: grid;
    grid-template-columns: 1.45fr 1fr 1.35fr;
    gap: 22px;
    padding: 22px 40px 0 50px;
  }
  .services-band ul { list-style: none; }
  .services-band li {
    font-family: "Oswald", sans-serif;
    font-weight: 500;
    font-size: 14px;
    line-height: 1.3;
    text-transform: uppercase;
    color: var(--band-text);
    position: relative;
    padding-left: 12px;
    margin-bottom: 4px;
  }
  .services-band li::before {
    content: "";
    position: absolute;
    left: 0; top: 7px;
    width: 5px; height: 5px;
    border-radius: 50%;
    background: var(--gold);
  }

  /* Back */
  .back-brand {
    position: absolute;
    inset: 0;
    display: flex;
    align-items: center;
    justify-content: center;
    gap: 20px;
  }
  .back-brand__square { width: 34px; height: 34px; background: var(--gold); }
  .back-brand__name {
    font-weight: 500;
    font-size: 46px;
    letter-spacing: 12px;
    color: var(--gold);
  }
</style>
</head>
<body>
  <section class="card card--front">
    <div class="brand-mark">
      <span class="brand-mark__square"></span>
      <span class="brand-mark__name">TORNVEL SKINHEAL</span>
    </div>

    <div class="identity">
      <h1 class="identity__name">FULL NAME</h1>
      <p class="identity__title">TITLE</p>
      <ul class="contacts">
        <li>
          <svg viewBox="0 0 24 24" aria-hidden="true"><path fill="#c9922e" d="M6.6 10.8c1.4 2.8 3.8 5.1 6.6 6.6l2.2-2.2c.3-.3.7-.4 1-.2 1.1.4 2.3.6 3.6.6.6 0 1 .4 1 1V20c0 .6-.4 1-1 1C10.6 21 3 13.4 3 4c0-.6.4-1 1-1h3.5c.6 0 1 .4 1 1 0 1.3.2 2.5.6 3.6.1.3 0 .7-.2 1z"/></svg>
          <span>555-014-2270</span>
        </li>
        <li>
          <svg viewBox="0 0 24 24" aria-hidden="true" fill="none" stroke="#c9922e" stroke-width="1.8"><circle cx="12" cy="12" r="9"/><ellipse cx="12" cy="12" rx="4" ry="9"/><path d="M3 12h18M4.5 7.5h15M4.5 16.5h15"/></svg>
          <span>www.tornvel-skinheal.com</span>
        </li>
        <li>
          <svg viewBox="0 0 24 24" aria-hidden="true"><path fill="none" stroke="#c9922e" stroke-width="2" d="M12 22s7-7.2 7-12.5A7 7 0 0 0 5 9.5C5 14.8 12 22 12 22z"/><circle cx="12" cy="9.5" r="2.5" fill="#c9922e"/></svg>
          <span>1820 Marlow Ave Ste 200<br>PMB 401187 Fairbrook, TX 75000</span>
        </li>
      </ul>
    </div>

    <h2 class="services-heading">OUR SERVICES</h2>
    <div class="services-band">
      <ul>
        <li>Hyperbaric Oxygen Therapy (HBO): A Cornerstone of Advanced Wound Care</li>
      </ul>
      <ul>
        <li>Debridement</li>
        <li>Advanced Wound Dressings</li>
      </ul>
      <ul>
        <li>Bio-Engineered Skin Substitutes</li>
        <li>Compression Therapy and Edema Management</li>
      </ul>
    </div>
  </section>

  <section class="card card--back">
    <div class="back-brand">
      <span class="back-brand__square"></span>
      <span class="back-brand__name">TORNVEL SKINHEAL</span>
    </div>
  </section>
</body>
</html>
```